Vantor Drift Shiners packaging design

We need a packaging design for Calder Trailworks LLC. The Brand Name is Vantor Drift Shiners, this is a fishing lure that was developed by a Inland Angling Honor Roll Hall inductee. We would like to see the designs that use the color green in the packaging. the final design should represent quality. excitement and Innovation. The Package size is 3 inches wide and 4 inches tall, this will be a pegged package so the front of the package is all that will need to be designed.
Target Market(s)
age 25-55 Male and Female
Logo Text
Tough and represents quality
Font styles to use
Requirements
Must have
- Vantor Drift Shiners as logo
- Tagline Inspired a World Record Fishing Title
- Notes not what to say but have it represented in the design: Bold and strength contemporary and sharp
Nice to have
- na
Should not have
- na

```html
<!DOCTYPE html>
<html lang="en">
<head>
<meta charset="utf-8">
<title>Vantor Drift Shiners – Peg Card</title>
<link rel="stylesheet" href="https://fonts.googleapis.com/css2?family=Exo+2:wght@700;800&family=Oswald:wght@500&display=swap">
<style>
  :root {
    --lime: #8cd600;
    --lime-deep: #7dbf00;
    --black: #0c0c0c;
    --white: #ffffff;
    --paper: #ffffff;
    --art-dark: #141414;
    --art-mid: #2a2f22;
  }
  html, body {
    margin: 0;
    width: 1200px;
    height: 1000px;
    overflow: hidden;
    background: var(--paper);
  }
  .canvas {
    position: relative;
    width: 1200px;
    height: 1000px;
  }
  .card-art {
    position: absolute;
    left: 0;
    top: 0;
    filter: drop-shadow(0 3px 6px rgba(0,0,0,0.35));
  }
  .brand-name {
    position: absolute;
    margin: 0;
    font-family: "Exo 2", sans-serif;
    font-weight: 800;
    color: var(--lime);
    text-transform: uppercase;
    line-height: 1.05;
    white-space: nowrap;
  }
  .brand-name span { display: block; }
  .card-brand {
    left: 180px;
    top: 327px;
    font-size: 31px;
    letter-spacing: 4px;
  }
  .tagline {
    position: absolute;
    left: 318px;
    top: 403px;
    width: 254px;
    height: 18px;
    margin: 0;
    font-family: "Oswald", sans-serif;
    font-weight: 500;
    font-style: italic;
    font-size: 11.5px;
    line-height: 18px;
    letter-spacing: 0.4px;
    text-align: center;
    color: var(--lime);
    text-transform: uppercase;
  }
  .maker {
    position: absolute;
    left: 174px;
    top: 745px;
    margin: 0;
    transform-origin: 0 0;
    transform: rotate(-90deg);
    font-family: "Exo 2", sans-serif;
    font-weight: 700;
    font-size: 17px;
    letter-spacing: 2.6px;
    color: var(--white);
    white-space: nowrap;
    text-transform: uppercase;
  }
  .sticker-brand {
    left: 652px;
    top: 452px;
    font-size: 38px;
    letter-spacing: 6px;
  }
</style>
</head>
<body>
<main class="canvas">

  <svg class="card-art" width="1200" height="1000" viewBox="0 0 1200 1000">
    <defs>
      <clipPath id="card-shape">
        <rect x="148" y="215" width="424" height="565" rx="24"/>
      </clipPath>
      <linearGradient id="artwork-tone" x1="0" y1="0" x2="1" y2="1">
        <stop offset="0" stop-color="var(--art-mid)"/>
        <stop offset="1" stop-color="var(--art-dark)"/>
      </linearGradient>
    </defs>

    <g clip-path="url(#card-shape)">
      <rect class="card-base" x="148" y="215" width="424" height="565" fill="var(--lime)"/>
      <rect class="side-rail" x="148" y="215" width="52" height="565" fill="var(--black)"/>
      <rect class="side-rail-top" x="148" y="215" width="57" height="98" fill="var(--black)"/>
      <polygon class="brand-band" points="148,318 572,318 572,400 203,400 148,458" fill="var(--black)"/>
      <line class="band-rule" x1="205" y1="313" x2="572" y2="313" stroke="var(--lime)" stroke-width="3"/>
      <polyline class="band-edge" points="148,468 203,405 205,405" fill="none" stroke="var(--lime)" stroke-width="3"/>
      <rect class="tagline-bar" x="318" y="403" width="254" height="18" fill="var(--black)"/>
      <rect class="blister-window" x="213" y="456" width="295" height="266" rx="14" fill="var(--lime-deep)"/>
      <rect class="bass-artwork" role="img"
            aria-label="Illustration of a leaping largemouth bass with open mouth, in black"
            x="340" y="535" width="240" height="250" rx="18"
            fill="url(#artwork-tone)" opacity="0.92"/>
    </g>

    <rect class="hang-slot" x="283" y="275" width="165" height="30" rx="15" fill="var(--paper)"/>
    <circle class="hang-notch" cx="365" cy="273" r="11" fill="var(--paper)"/>

    <rect class="sticker-shadow" x="606" y="446" width="530" height="112" rx="18" fill="var(--black)" stroke="var(--white)" stroke-width="3"/>
    <rect class="sticker" x="612" y="440" width="520" height="104" rx="16" fill="var(--black)"/>
  </svg>

  <h1 class="brand-name card-brand"><span>Vantor Drift</span><span>Shiners</span></h1>
  <p class="tagline">Inspired a World Record Fishing Title</p>
  <p class="maker">Calder Trailworks LLC.</p>

  <p class="brand-name sticker-brand"><span>Vantor Drift</span><span>Shiners</span></p>

</main>
</body>
</html>
```